Personal Injury Lawyer Billboard

I would like a design created featuring the image of the lawyer centered in the middle of the design.
To the left of the lawyer's image it should read "INJURED?"
To the right of the lawyer's image, it should read "CALL BRUNO!"
Under Call Bruno, include the phone number 318-555-0187.
At the bottom of the design include the lawyers information "Bruno Pemberly Accident & Injury Lawyers"
PLEASE REMOVED THE BACKGROUND IMAGERY OF THE PHOTO SUBMITTED. Also, the colors for this design should match the colors shown in the logo (navy, white and relective soft gold). Please use those color combinations in ways that best stand out.

```html
<!DOCTYPE html>
<html lang="en">
<head>
<meta charset="utf-8">
<title>Bruno Pemberly Accident &amp; Injury Lawyers – Billboard</title>
<link rel="stylesheet" href="https://fonts.googleapis.com/css2?family=Lato:wght@700;900&family=Noto+Serif:wght@700&family=Oswald:wght@500&display=swap">
<style>
  :root {
    --navy-deep: #031a4f;
    --navy: #0a2a6e;
    --navy-bright: #1450a8;
    --stripe: #1a5bb8;
    --white: #ffffff;
    --gold: #cfab43;
    --ink: #0b0b0b;
  }
  * { margin: 0; padding: 0; box-sizing: border-box; }
  html, body { width: 1200px; height: 960px; overflow: hidden; background: var(--navy-deep); }
  .billboard {
    position: relative;
    width: 1200px;
    height: 960px;
    overflow: hidden;
    background: radial-gradient(ellipse at 30% 30%, var(--navy) 0%, var(--navy-deep) 75%);
  }
  .backdrop-stripes { position: absolute; inset: 0; width: 1200px; height: 816px; }
  .firm-name {
    position: absolute;
    top: 26px;
    left: 0;
    width: 1200px;
    text-align: center;
    font-family: "Oswald", sans-serif;
    font-weight: 500;
    color: var(--white);
    line-height: 1;
  }
  .firm-name .firm-title { display: block; font-size: 48px; letter-spacing: 0.5px; }
  .firm-name .firm-sub { display: block; font-size: 26px; margin-top: 14px; letter-spacing: 0.3px; }
  .headline {
    font-family: "Noto Serif", serif;
    font-weight: 700;
    font-size: 54px;
    color: var(--white);
    line-height: 1;
    white-space: nowrap;
  }
  .pitch-left {
    position: absolute;
    top: 350px;
    left: 40px;
    width: 340px;
    text-align: center;
  }
  .pitch-right {
    position: absolute;
    top: 350px;
    left: 780px;
    width: 400px;
    text-align: center;
  }
  .phone-number {
    margin-top: 50px;
    font-family: "Lato", sans-serif;
    font-weight: 700;
    font-size: 38px;
    line-height: 1;
    color: var(--white);
    letter-spacing: 0.5px;
    white-space: nowrap;
  }
  .lawyer-portrait {
    position: absolute;
    left: 420px;
    top: 204px;
    width: 356px;
    height: 612px;
    border-radius: 140px 140px 0 0;
    background: linear-gradient(180deg, #3b3f55 0%, #1c2552 45%, #121a45 100%);
  }
  .footer-band {
    position: absolute;
    left: 0;
    top: 816px;
    width: 1200px;
    height: 144px;
    background: var(--gold);
    display: flex;
    align-items: center;
    justify-content: center;
  }
  .footer-band .footer-firm {
    font-family: "Lato", sans-serif;
    font-weight: 700;
    font-size: 54px;
    color: var(--ink);
    white-space: nowrap;
    letter-spacing: -0.3px;
  }
</style>
</head>
<body>
<main class="billboard">
  <svg class="backdrop-stripes" viewBox="0 0 1200 816" aria-hidden="true">
    <defs>
      <linearGradient id="stripeGlow" x1="0" y1="1" x2="1" y2="0">
        <stop offset="0" stop-color="#1450a8" stop-opacity="0.15"/>
        <stop offset="1" stop-color="#1a5bb8" stop-opacity="0.7"/>
      </linearGradient>
    </defs>
    <polygon points="560,816 1200,150 1200,330 720,816" fill="url(#stripeGlow)" opacity="0.55"/>
    <polygon points="820,816 1200,420 1200,560 960,816" fill="url(#stripeGlow)" opacity="0.6"/>
    <polygon points="640,0 900,0 300,816 20,816" fill="#0d3486" opacity="0.35"/>
    <polygon points="1000,0 1200,0 1200,40 700,560 620,560" fill="url(#stripeGlow)" opacity="0.45"/>
    <line x1="760" y1="816" x2="1200" y2="360" stroke="#3d86d8" stroke-width="2" opacity="0.5"/>
    <line x1="990" y1="816" x2="1200" y2="600" stroke="#3d86d8" stroke-width="2" opacity="0.4"/>
  </svg>

  <header class="firm-name">
    <span class="firm-title">BRUNO PEMBERLY</span>
    <span class="firm-sub">ACCIDENT &amp; INJURY LAWYERS</span>
  </header>

  <div class="pitch-left">
    <h2 class="headline">INJURED?</h2>
  </div>

  <div class="lawyer-portrait" role="img" aria-label="Cut-out photo of the lawyer in a navy suit and green tie, smiling with a raised fist"></div>

  <div class="pitch-right">
    <h2 class="headline">CALL BRUNO!</h2>
    <p class="phone-number">318-555-0187</p>
  </div>

  <footer class="footer-band">
    <p class="footer-firm">Bruno Pemberly Accident &amp; Injury Lawyers</p>
  </footer>
</main>
</body>
</html>
```